Financial Planning Business needs a business card design

We need a business card design that is for a new financial planning business based in Australia. We provide financial planning advice such as retirement planning, wealth creation, asset protection.

Attached is the logo design. On the front side of the business card needs to incorporate the following:
- adviser name
- adviser title (ie Managing Director)
- address
- phone number
- email
- website address

Ideally it should also have the business name and logo

On the back of the card I would like this to be black in colour with the business name and logo

I have been advised the font is "Cinzel" (regular and bold)

Industry/Entity Type

Financial

Requirements
Must have
• Logo and business name

Format to have as follows:
Tom xxxxxxxx
Managing Director / Senior Financial Adviser
address
phone email
website

```html
<!DOCTYPE html>
<html lang="en">
<head>
<meta charset="utf-8">
<title>Meridian Wealth Planning – Business Card</title>
<link href="https://fonts.googleapis.com/css2?family=Cinzel:wght@400;700&family=Open+Sans:wght@400;600;700&display=swap" rel="stylesheet">
<style>
  :root {
    --backdrop: #e6e6e6;
    --sky: #1b8fd6;
    --navy: #1d3466;
    --back-black: #111214;
    --paper: #f7f7f7;
    --ink: #1f2a3a;
    --muted: #8a8f96;
  }
  * { box-sizing: border-box; margin: 0; padding: 0; }
  html, body {
    width: 1200px; height: 1200px; overflow: hidden;
    background: var(--backdrop);
  }
  .sheet {
    width: 1200px; height: 1200px;
    display: flex; flex-direction: column;
    align-items: center; justify-content: center; gap: 70px;
  }
  .card {
    position: relative; width: 620px; height: 376px; overflow: hidden;
    box-shadow: 0 10px 28px rgba(0,0,0,.16);
  }

  /* Brand side (back) */
  .card--brand { background: var(--back-black); }
  .brand-band {
    position: absolute; left: 0; right: 0; top: 118px; height: 140px;
    background: var(--navy);
    display: flex; align-items: center; justify-content: center; gap: 16px;
  }
  .brand-square { width: 30px; height: 30px; background: var(--sky); flex: none; }
  .brand-name {
    font-family: "Cinzel", serif; font-weight: 400;
    font-size: 30px; letter-spacing: 1px; color: var(--sky);
    white-space: nowrap;
  }

  /* Contact side (front) */
  .card--contact { background: var(--paper); }
  .contact-lower {
    position: absolute; left: 0; right: 0; bottom: 0; height: 160px;
    background: var(--sky);
  }
  .adviser {
    position: absolute; left: 38px; top: 40px;
    font-family: "Open Sans", sans-serif;
  }
  .adviser-name { font-size: 21px; font-weight: 700; color: var(--sky); }
  .adviser-title { font-size: 14px; color: var(--muted); line-height: 1.4; margin-top: 4px; }
  .contact-brand {
    position: absolute; right: 36px; top: 150px;
    display: flex; align-items: center; gap: 12px;
  }
  .contact-brand .brand-square { width: 22px; height: 22px; background: var(--navy); }
  .contact-brand .brand-name { font-size: 22px; color: var(--sky); }
  .address {
    position: absolute; left: 38px; top: 248px;
    font-family: "Open Sans", sans-serif; font-size: 14px; line-height: 1.55;
    color: var(--ink);
  }
  .contact-list {
    position: absolute; right: 40px; top: 246px; list-style: none;
    font-family: "Open Sans", sans-serif; font-size: 15px; color: var(--ink);
  }
  .contact-list li { display: flex; align-items: center; gap: 10px; line-height: 1.6; }
  .contact-list svg { width: 16px; height: 16px; flex: none; }
</style>
</head>
<body>
<main class="sheet">

  <section class="card card--brand" aria-label="Card back">
    <div class="brand-band">
      <span class="brand-square"></span>
      <span class="brand-name">Meridian Wealth Planning</span>
    </div>
  </section>

  <section class="card card--contact" aria-label="Card front">
    <div class="contact-lower"></div>

    <div class="adviser">
      <p class="adviser-name">Tom xxxxxxxx</p>
      <p class="adviser-title">Managing Director<br>Senior Financial Adviser</p>
    </div>

    <div class="contact-brand">
      <span class="brand-square"></span>
      <span class="brand-name">Meridian Wealth Planning</span>
    </div>

    <p class="address">xxxxxxxxxxx xxxxxxxxxx, xxx,<br>xxxxxx, xxxxxxxx, xxx xxx 3212</p>

    <ul class="contact-list">
      <li>
        <svg viewBox="0 0 16 16" aria-hidden="true"><circle cx="8" cy="8" r="7.5" fill="#1f2a3a"/><rect x="5.5" y="3.5" width="5" height="9" rx="1" fill="#fff"/></svg>
        xxxxxxxxxx
      </li>
      <li>
        <svg viewBox="0 0 16 16" aria-hidden="true"><circle cx="8" cy="8" r="7.5" fill="#1f2a3a"/><rect x="4" y="5" width="8" height="6" fill="#fff"/><path d="M4 5l4 3.5L12 5" stroke="#1f2a3a" stroke-width="1" fill="none"/></svg>
        aaaaaa@xxxxxxxx.com
      </li>
      <li>
        <svg viewBox="0 0 16 16" aria-hidden="true"><circle cx="8" cy="8" r="7.5" fill="#1f2a3a"/><circle cx="8" cy="8" r="4.5" fill="none" stroke="#fff" stroke-width="1"/><path d="M3.5 8h9M8 3.5c-2 2.5-2 6.5 0 9M8 3.5c2 2.5 2 6.5 0 9" stroke="#fff" stroke-width="1" fill="none"/></svg>
        www.xxxxxxxxx.com
      </li>
    </ul>
  </section>

</main>
</body>
</html>
```